The maple crew

I want it as prefession and attractive as possible we are a lawnmowing business

Phone number 605-318-2264
Name- Carlos Whitfield
Email- themaplecrewsd@fernpost.com

```html
<!DOCTYPE html>
<html lang="en">
<head>
<meta charset="UTF-8">
<title>The Maple Crew – Business Card</title>
<link rel="stylesheet" href="https://fonts.googleapis.com/css2?family=Roboto:wght@400;700;900&display=swap">
<style>
  :root {
    --backdrop: #efe9df;
    --card-white: #ffffff;
    --card-green: #0d6135;
    --green-deep: #126b36;
    --green-bright: #5fbf4c;
    --card-shadow: 0 3px 10px rgba(60, 45, 20, 0.18);
  }
  * { margin: 0; padding: 0; box-sizing: border-box; }
  html, body {
    width: 1200px;
    height: 1200px;
    overflow: hidden;
    background: var(--backdrop);
    font-family: "Roboto", Arial, sans-serif;
  }
  .canvas {
    position: relative;
    width: 1200px;
    height: 1200px;
  }
  .card {
    position: absolute;
    left: 299px;
    width: 602px;
    box-shadow: var(--card-shadow);
  }
  .card--front {
    top: 238px;
    height: 347px;
    background: var(--card-white);
  }
  .card--back {
    top: 622px;
    height: 360px;
    background: var(--card-green);
  }
  .brand {
    position: absolute;
    left: 0;
    right: 0;
    height: 137px;
    display: flex;
    align-items: center;
    justify-content: center;
    gap: 16px;
  }
  .card--front .brand { top: 49px; }
  .card--back .brand { top: 107px; }
  .brand__mark {
    width: 34px;
    height: 34px;
    flex: none;
    background: var(--green-bright);
  }
  .brand__name {
    font-weight: 900;
    font-size: 54px;
    letter-spacing: 0.5px;
    text-transform: uppercase;
    line-height: 1;
    white-space: nowrap;
    color: var(--green-deep);
  }
  .card--back .brand__name { color: var(--green-bright); }
  .contact {
    position: absolute;
    top: 217px;
    left: 0;
    right: 0;
    text-align: center;
    color: var(--green-deep);
  }
  .contact__name {
    font-weight: 700;
    font-size: 36px;
    line-height: 44px;
    margin-bottom: 14px;
  }
  .contact__line {
    font-weight: 400;
    font-size: 19px;
    line-height: 29px;
  }
</style>
</head>
<body>
  <main class="canvas">
    <section class="card card--front">
      <div class="brand">
        <span class="brand__mark"></span>
        <span class="brand__name">The maple crew</span>
      </div>
      <div class="contact">
        <p class="contact__name">Carlos Whitfield</p>
        <p class="contact__line">Phone: 605-318-2264</p>
        <p class="contact__line">Email: themaplecrewsd@fernpost.com</p>
      </div>
    </section>

    <section class="card card--back">
      <div class="brand">
        <span class="brand__mark"></span>
        <span class="brand__name">The maple crew</span>
      </div>
    </section>
  </main>
</body>
</html>
```